Design a landing page

We have a logo, we have colours in mind. What we need is to create a typical one-page landing page that would look nicely on both PC and mobile devices/tablets.

Typical layout - logo top left, top right - shop/client area buttons (links will open to different websites), informational area in the middle - image on the left + text on the right then image on the right + text on the left etc., then text links at the bottom (T&S, Cookie policy, privacy policy etc.).

Page must have cookie notification as per EU law.

We will also need help in preparing photos/images (up to 8) for the website.

End result should be either a Wordpress theme (preferred - so we can install it from wordpress control panel) or HTML/CSS page source. All scripts/images/files should be included - no external links to js/image libraries please.

The photo of the device attached. Primary users will be home users with placement on the ceiling, Minority of users will be business/commercial users with wall placements. Device is meant to monitor climat in the premises (Temperature, humidity, dew point) and alert users if readings are not within allowed range.

Need extra days to review

Industry/Entity Type

Microclimate Monitoring in premises

Coding

Coded - Design and coding required

Number of Pages Required

1 page

Colors
0054AA
0677BA
7BADD7
CADEEF
E8F1F8
0094D4
00A9DD
6FCCEA
C7EBF8
E9F6FB

Requirements
Must have
• White background, layout as described unless better option offered and accepted. Must have cookie warning.

```html
<!DOCTYPE html>
<html lang="en">
<head>
<meta charset="UTF-8">
<title>Climate Monitoring Features</title>
<link href="https://fonts.googleapis.com/css2?family=Arimo:wght@400;700&display=swap" rel="stylesheet">
<style>
  :root {
    --blue-dark: #0054AA;
    --blue-accent: #0094D4;
    --blue-pale: #C7EBF8;
    --band-bg: #F3F8FC;
    --text: #111111;
    --white: #FFFFFF;
  }
  * { margin: 0; padding: 0; box-sizing: border-box; }
  html, body {
    width: 1200px; height: 540px; overflow: hidden;
    background: var(--white);
    font-family: "Arimo", Arial, sans-serif;
    color: var(--text);
  }
  .page { position: relative; width: 1200px; height: 540px; }
  .feature-band {
    position: absolute; left: 3px; top: 124px; width: 1194px; height: 189px;
    background: var(--band-bg);
  }
  .media {
    position: absolute; width: 338px; height: 126px;
    background: var(--blue-pale);
  }
  .media-photo { position: absolute; left: 0; top: 0; width: 253px; height: 100%; }
  .photo-charts { background: linear-gradient(90deg, #f2f2f2 0%, #f7e3e3 45%, #e9573c 75%, #c7dde8 100%); }
  .photo-dashboard { background: linear-gradient(120deg, #1c2733 0%, #3b5c78 40%, #b8652e 70%, #2a2f3a 100%); }
  .photo-install { background: linear-gradient(90deg, #c9c6c0 0%, #8a8784 35%, #e6e3de 65%, #d8d4cc 100%); }
  .feature-text { position: absolute; }
  .feature-title { font-size: 15px; font-weight: 700; line-height: 1.1; }
  .feature-desc { font-size: 10px; line-height: 1.25; }
  .cookie-bar {
    position: absolute; left: 3px; top: 501px; width: 1194px; height: 39px;
    background: var(--blue-dark); color: var(--white);
    display: flex; align-items: center; justify-content: space-between;
    padding: 0 6px 0 3px; font-size: 10px;
  }
  .cookie-accept {
    background: var(--blue-accent); color: var(--white);
    border: none; font-family: inherit; font-size: 8.5px;
    width: 44px; height: 19px;
  }
</style>
</head>
<body>
<div class="page">
  <div class="feature-band"></div>

  <div class="media" style="left:251px; top:0; height:92px;">
    <div class="media-photo photo-charts" role="img" aria-label="Temperature charts and a heat map of climate readings"></div>
  </div>
  <div class="feature-text" style="left:608px; top:15px;">
    <h2 class="feature-title">Real-Time Monitoring</h2>
    <p class="feature-desc">Get instant updates on climate conditions inside your premises.</p>
  </div>

  <div class="feature-text" style="left:251px; top:205px;">
    <h2 class="feature-title">Smart Alerts</h2>
    <p class="feature-desc">Receive alerts when readings exceed safe thresholds.</p>
  </div>
  <div class="media" style="left:608px; top:155px;">
    <div class="media-photo photo-dashboard" role="img" aria-label="Weather dashboard showing temperature, humidity and alert readings"></div>
  </div>

  <div class="media" style="left:251px; top:345px;">
    <div class="media-photo photo-install" role="img" aria-label="Woman mounting a climate sensor on a living room wall"></div>
  </div>
  <div class="feature-text" style="left:608px; top:395px;">
    <h2 class="feature-title">Easy Installation</h2>
    <p class="feature-desc">Ceiling or wall placement for homes and businesses.</p>
  </div>

  <div class="cookie-bar">
    <span>We use cookies to improve your experience.</span>
    <button class="cookie-accept">Accept</button>
  </div>
</div>
</body>
</html>
```